Marlowe's Larder home based food retailer

I need a label for my new home based business making granola. Other products like cookies, jams and relishes in future.

I imagine the original logo in dark or mid (dusty) blue with white printing.

A logo that can be easily be recognised across a variety of product lines. IE: the same design that can be different colours for other flavours of granola. EG: green for fig & pistachio, red for cherry & chocolate

The granola will be packaged in resealable kraft paper bags.

The logo and product name will be on the front and other information on the back. IE: ingredients, nutritional panel, contact details. See below

The whole label will measure 210mm (L) x 80mm (W), with 80mm on the front and 130mm on the back. See attached

FRONT:
Marlowe's Larder
ORIGINAL GRANOLA
400g

BACK:
Marlowe's Larder
ORIGINAL GRANOLA
Delicious, all natural granola made in the beautiful Macedon Ranges. Serve with your choice of milk, fruit or yoghurt. Store in an airtight container.

INGREDIENTS:
Oats (print in bold), honey, coconut oil, pumpkin seeds, almonds(print in bold), sultanas, sunflower seeds, linseeds, vanilla extract, cinnamon, sea salt.
Contains gluten and nuts (print in bold)

Made in Australia using local and imported ingredients.

Contact:
marloweslarder.com.au
info@marloweslarder.com.au
facebook logo
instagram logo

NUTRITIONAL PANEL (see attached)

Many thanks,
Marlowe

Target Market(s)

For those who are seeking a locally homemade, wholesome breakfast or snack. Cafes, market stalls, fruit & veg distributorss

Industry/Entity Type

granola production

Logo Text

Marlowe's Larder. Original Granola. 400g

Logo styles of interest
Pictorial/Combination Logo
Wordmark Logo
Font styles to use
Serif
Script

Colors
0054AA
0677BA
7BADD7
CADEEF
E8F1F8
00AB8E
00BBA5
67D7C9
C6EFE9
E9F9F6
EE7325
F08F49
F5BC92
FAE3D3
FDF4ED
EB3D1F
EC4F4E
F09395
F8D3D4
FCEDEE

Requirements
Must have
• Pretty, yet simple logo
Nice to have
• A variety of options with background design or a little symbol. Prefer dusty colours
Should not have
• too fancy or fussy design, bright colours

```html
<!DOCTYPE html>
<html lang="en">
<head>
<meta charset="utf-8">
<title>Marlowe's Larder – Original Granola Label</title>
<link rel="stylesheet" href="https://fonts.googleapis.com/css2?family=Cinzel:wght@400;600&family=Poppins:wght@400;500;600&display=swap">
<style>
  :root {
    --dusty-blue: #5f6e8a;
    --wreath-tone: #4a5775;
    --ink-white: #ffffff;
    --caption: #5b6a87;
    --page: #ffffff;
    --serif: "Cinzel", "Times New Roman", serif;
    --sans: "Poppins", Arial, sans-serif;
  }
  * { box-sizing: border-box; margin: 0; padding: 0; }
  html, body { width: 1200px; height: 1200px; overflow: hidden; background: var(--page); }
  .canvas { position: relative; width: 1200px; height: 1200px; overflow: hidden; background: var(--page); }

  /* shared */
  .wreath {
    position: absolute; border-radius: 50%;
    background: radial-gradient(circle, transparent 0 78%, rgba(74,87,117,.55) 80%, rgba(74,87,117,.25) 92%, transparent 100%);
  }
  .brand { position: absolute; left: 0; right: 0; text-align: center; color: var(--ink-white); font-family: var(--serif); font-weight: 400; line-height: 1.05; }
  .product { position: absolute; left: 50%; transform: translateX(-50%); color: var(--ink-white); font-family: var(--serif); text-align: center; line-height: 1.1; border-top: 2px solid var(--ink-white); border-bottom: 2px solid var(--ink-white); }
  .weight { position: absolute; left: 0; right: 0; text-align: center; color: var(--ink-white); font-family: var(--sans); font-weight: 600; }

  /* front panel */
  .front-panel { position: absolute; left: 551px; top: 0; width: 649px; height: 954px; background: var(--dusty-blue); }
  .front-panel .wreath { left: 110px; top: 268px; width: 420px; height: 420px; }
  .front-panel .brand { top: 398px; font-size: 50px; }
  .front-panel .product { top: 548px; width: 198px; font-size: 22px; letter-spacing: 2px; padding: 3px 0 4px; border-width: 2px; }
  .front-panel .weight { top: 612px; font-size: 20px; }

  /* full label layout */
  .label { position: absolute; left: 169px; top: 245px; width: 270px; height: 709px; background: var(--dusty-blue); }
  .label-front { position: absolute; left: 0; top: 440px; width: 270px; height: 269px; border-top: 1.5px dotted rgba(255,255,255,.6); }
  .label-front .wreath { left: 40px; top: 18px; width: 200px; height: 200px; }
  .label-front .brand { top: 58px; font-size: 24px; }
  .label-front .product { top: 132px; width: 96px; font-size: 11px; letter-spacing: 1px; padding: 1px 0 2px; border-width: 1px; }
  .label-front .weight { top: 162px; font-size: 10px; }

  .label-back { position: absolute; left: 0; top: 0; width: 270px; height: 440px; transform: rotate(180deg); color: var(--ink-white); font-family: var(--sans); }
  .back-title { position: absolute; top: 26px; left: 0; right: 0; text-align: center; font-family: var(--serif); font-size: 15px; font-weight: 600; letter-spacing: .5px; }
  .back-sub { position: absolute; top: 46px; left: 0; right: 0; text-align: center; font-family: var(--serif); font-size: 9px; letter-spacing: 1px; }
  .back-weight { position: absolute; top: 58px; left: 0; right: 0; text-align: center; font-size: 8px; }
  .blurb, .ingredients { position: absolute; left: 20px; right: 20px; text-align: center; font-size: 7.4px; line-height: 1.45; }
  .blurb { top: 86px; }
  .divider { position: absolute; left: 90px; right: 90px; border-top: 1.5px dotted rgba(255,255,255,.7); }
  .divider.one { top: 133px; }
  .divider.two { top: 226px; }
  .ingredients-head { position: absolute; top: 146px; left: 0; right: 0; text-align: center; font-size: 8px; font-weight: 500; letter-spacing: .5px; }
  .ingredients { top: 160px; }
  .allergens { position: absolute; top: 200px; left: 0; right: 0; text-align: center; font-size: 7.6px; font-weight: 600; }
  .origin { position: absolute; top: 240px; left: 16px; width: 238px; height: 24px; background: var(--ink-white); color: var(--dusty-blue); border-radius: 3px; font-size: 6.6px; display: flex; align-items: center; gap: 8px; padding: 0 8px; }
  .origin-badge { width: 13px; height: 13px; background: var(--dusty-blue); clip-path: polygon(50% 0, 100% 100%, 0 100%); flex: none; }

  .nutrition { position: absolute; top: 282px; left: 127px; width: 134px; height: 146px; background: var(--ink-white); color: var(--dusty-blue); padding: 5px 6px; font-size: 6px; line-height: 1.35; }
  .nutrition h3 { font-size: 7px; font-weight: 600; border-bottom: 1px solid var(--dusty-blue); padding-bottom: 2px; margin-bottom: 2px; }
  .nutrition table { width: 100%; border-collapse: collapse; }
  .nutrition th { font-weight: 400; text-align: right; border-bottom: 1px solid var(--dusty-blue); }
  .nutrition td { text-align: right; }
  .nutrition td:first-child, .nutrition th:first-child { text-align: left; }
  .nutrition .main td:first-child { font-weight: 600; }
  .serving { border-bottom: 1px solid var(--dusty-blue); padding-bottom: 2px; margin-bottom: 2px; }

  .contact { position: absolute; left: 6px; top: 380px; width: 112px; font-size: 6.6px; line-height: 1.6; border-top: 1px solid rgba(255,255,255,.8); padding-top: 4px; }
  .social { position: absolute; left: 30px; top: 418px; display: flex; gap: 6px; }
  .social span { width: 8px; height: 8px; border-radius: 50%; background: var(--ink-white); }

  .note { position: absolute; top: 1043px; left: 0; right: 0; text-align: center; font-family: var(--sans); font-size: 17px; color: var(--caption); letter-spacing: .3px; }
</style>
</head>
<body>
<div class="canvas">

  <section class="label" aria-label="Full wrap-around label">
    <div class="label-back">
      <h2 class="back-title">MARLOWE'S LARDER</h2>
      <p class="back-sub">ORIGINAL GRANOLA</p>
      <p class="back-weight">400g</p>
      <p class="blurb">Delicious, all natural granola made in the beautiful Macedon Ranges. Serve with your choice of milk, fruit or yoghurt. Store in an airtight container.</p>
      <div class="divider one"></div>
      <p class="ingredients-head">INGREDIENTS:</p>
      <p class="ingredients"><strong>Oats</strong>, honey, coconut oil, pumpkin seeds, <strong>almonds</strong>, sultanas, sunflower seeds, linseeds, vanilla extract, cinnamon, sea salt.</p>
      <p class="allergens">Contains gluten and nuts.</p>
      <div class="divider two"></div>
      <div class="origin"><span class="origin-badge" role="img" aria-label="Origin badge"></span>Made in Australia using local and imported ingredients</div>
      <div class="nutrition">
        <h3>NUTRITION INFORMATION</h3>
        <div class="serving">Servings per package: 8<br>Serving size: 50 g</div>
        <table>
          <tr><th></th><th>Per Serving</th><th>Per 100g</th></tr>
          <tr class="main"><td>Energy</td><td>972 kJ</td><td>1940 kJ</td></tr>
          <tr class="main"><td>Protein</td><td>5.1 g</td><td>10.2 g</td></tr>
          <tr class="main"><td>Total Fat</td><td>13.1 g</td><td>26.2 g</td></tr>
          <tr><td>– saturated</td><td>5.2 g</td><td>10.4 g</td></tr>
          <tr class="main"><td>Carbohydrate</td><td>21.9 g</td><td>43.8 g</td></tr>
          <tr><td>– sugars</td><td>11.3 g</td><td>22.5 g</td></tr>
          <tr class="main"><td>Sodium</td><td>25 mg</td><td>50 mg</td></tr>
        </table>
      </div>
      <div class="contact">marloweslarder.com.au<br>info@marloweslarder.com.au</div>
      <div class="social" aria-label="Social links"><span></span><span></span></div>
    </div>

    <div class="label-front">
      <div class="wreath" role="img" aria-label="Floral wreath illustration with blossoms and leafy sprigs"></div>
      <h2 class="brand">Marlowe's<br>Larder</h2>
      <p class="product">ORIGINAL<br>GRANOLA</p>
      <p class="weight">400g</p>
    </div>
  </section>

  <section class="front-panel" aria-label="Front of label, enlarged">
    <div class="wreath" role="img" aria-label="Floral wreath illustration with blossoms and leafy sprigs"></div>
    <h1 class="brand">Marlowe's<br>Larder</h1>
    <p class="product">ORIGINAL<br>GRANOLA</p>
    <p class="weight">400g</p>
  </section>

  <p class="note">Please remove the manufacture and expiry date. I will be using separate stickers.</p>
</div>
</body>
</html>
```